Business Card Design

We Need a business card design for my company based in Tv Radio and music Productions and hunt Talent.

Industry/Entity Type

Business

Contact Information for Business Card

BrentaVue Production's, Teodor Vignoles,Cell Phone 318 4957310
Musician, Productor, Hunt Talent. Miami Fla. www.brentavue.net Mail. teodorvignoles@mailvana.com

```html
<!DOCTYPE html>
<html lang="en">
<head>
<meta charset="utf-8">
<title>BrentaVue Production's – Business Card</title>
<link rel="stylesheet" href="https://fonts.googleapis.com/css2?family=Open+Sans:wght@400;600;700&family=Courgette&display=swap">
<style>
  :root {
    --page-bg: #d9d9d9;
    --card-black: #141414;
    --card-black-sheen: #3a3a3a;
    --purple: #7b3596;
    --purple-deep: #5e2378;
    --mauve-panel: #9a5fa6;
    --star-yellow: #f6c92a;
    --white: #ffffff;
    --soft-white: #efe3f3;
  }
  * { box-sizing: border-box; margin: 0; padding: 0; }
  html, body {
    width: 1200px; height: 900px; overflow: hidden;
    background: var(--page-bg);
    font-family: "Open Sans", Arial, sans-serif;
  }
  .canvas {
    position: relative; width: 1200px; height: 900px;
  }
  .card {
    position: absolute; left: 260px;
    width: 680px; height: 388px;
    overflow: hidden;
    box-shadow: 0 10px 26px rgba(0,0,0,.28);
  }
  .card--front {
    top: 40px;
    background:
      repeating-linear-gradient(0deg, rgba(255,255,255,.025) 0 1px, transparent 1px 3px),
      radial-gradient(ellipse at 50% 35%, var(--card-black-sheen), var(--card-black) 70%);
    display: flex; align-items: center; justify-content: center;
  }
  .card--back {
    top: 472px;
    background: var(--purple);
    color: var(--white);
  }
  .brand-mark {
    display: flex; align-items: center; gap: 18px;
  }
  .brand-mark__dot {
    width: 64px; height: 64px; border-radius: 50%;
    background: var(--star-yellow);
  }
  .brand-mark__name {
    font-weight: 700; font-size: 44px; color: var(--white);
    line-height: 1;
  }
  .card--back .brand-mark {
    position: absolute; right: 46px; top: 96px; gap: 12px;
  }
  .card--back .brand-mark__dot { width: 44px; height: 44px; }
  .card--back .brand-mark__name { font-size: 30px; }
  .back-panel {
    position: absolute; left: 0; top: 0; width: 680px; height: 388px;
  }
  .identity {
    position: absolute; left: 40px; top: 28px;
  }
  .identity__name {
    font-size: 30px; font-weight: 600; letter-spacing: 2px;
  }
  .identity__role {
    font-size: 12px; letter-spacing: .5px; margin-top: 2px;
  }
  .contact {
    list-style: none; margin-top: 20px;
    font-size: 13px; line-height: 1.45; color: var(--soft-white);
  }
  .company {
    position: absolute; right: 40px; bottom: 36px; text-align: right;
  }
  .company__name {
    font-family: "Courgette", cursive;
    font-size: 28px; color: var(--soft-white);
    letter-spacing: 1px;
    text-shadow: 0 0 6px rgba(255,255,255,.5);
  }
  .company__city {
    font-size: 11px; color: var(--soft-white); opacity: .75;
  }
</style>
</head>
<body>
<main class="canvas">
  <section class="card card--front" aria-label="Card front">
    <div class="brand-mark">
      <span class="brand-mark__dot"></span>
      <span class="brand-mark__name">Brenta's Show</span>
    </div>
  </section>

  <section class="card card--back" aria-label="Card back">
    <svg class="back-panel" viewBox="0 0 680 388" aria-hidden="true">
      <polygon points="0,0 210,0 210,40 470,92 210,150 175,260 150,388 0,388" fill="var(--purple-deep)"/>
      <polygon points="0,0 200,0 200,36 440,92 200,140 160,255 135,388 0,388" fill="var(--mauve-panel)"/>
    </svg>
    <div class="identity">
      <h1 class="identity__name">Teodor Vignoles</h1>
      <p class="identity__role">Musician, Productor, Hunt Talent</p>
      <ul class="contact">
        <li>phone: 318 4957310</li>
        <li>web: www.brentavue.net</li>
        <li>email: teodorvignoles@mailvana.com</li>
      </ul>
    </div>
    <div class="brand-mark">
      <span class="brand-mark__dot"></span>
      <span class="brand-mark__name">Brenta's Show</span>
    </div>
    <div class="company">
      <p class="company__name">BrentaVue Production's</p>
      <p class="company__city">Miami Fla</p>
    </div>
  </section>
</main>
</body>
</html>
```